Alcohol Marketing website

Home page and information page design, details as follows

CLIENT PURPOSE
Increase online visibility and create good contacts to increase business.

SERVICES
Drinks Marketing Consultancy
Brand Representation
Spirit Brand Sales & Marketing
Brand Development
Brand Distribution
Brand Launch & Introductions

COMPETITION
merrycasks.co.uk -
talvoranbrands.co.uk -

WEBSITE(S) CLIENT LIKES
Small competitors I admire:
http://www.merrycasks.co.uk/main.htm
http://www.talvoranbrands.com
http://www.vaultpicks.co.uk/spiritsliqueursbybrand.php
http://www.quellomarks.com/page1.html
http://www.zirnopaxtra.co.uk/index.asp

Nice page layout:
http://www.kvworks.com/
http://www.dmhallies.com/
http://www.pelvik.com/index.cfm?do=pelvik.home

WEBSITE CLIENT DOES NOT LIKE
http://www.tidemarque.com/
http://www.parlour-labels.com/
http://www.yonderpours.co.uk/aboutUs.html
http://www.graincorkhouse.com/
http://www.orbitmarques.co.uk/default.asp
http://www.summit-labels.co.uk/start.htm
http://www.durlay.co.uk/
http://www.pkcasks.com/default2.aspx
http://www.quaff-marques.co.uk/mainpage.aspx

COMPANY LOGO
Customer has a company logo (Supplied)

COLOURS:
Blue
White

STRAPLINE:
No

WEBSITE THEME: Marketing

IMAGES THAT BEST REFLECT THE COMPANY:
Spirits / Drinks

HEADER IMAGE:
Spirits / Brands

PAGES:
home
strength& flavour
a little about us
our spirit marketing
big brand success
speak to us

USER JOURNEYS:
General Service > Land on website >Navigation > Info Pages > Contact Form
Questions > Land on website > Message Banners > Info Pages > Contact Form
Contact > Land on website > Clear Telephone / Email Banner > Contact Form

CALL TO ACTION BANNER:
If you need help making your drink the next big brand, speak to us today.

KEYWORDS THAT RELATE TO THE BUSINESS:
brand marketing
drinks marketing
spirits marketing
brand marketing strategy
alcoholic drinks marketing
Drinks Brand Development

LOCATION(S):
United Kingdom -
Worldwide -

Target Market(s)

Male & Female
30-60
Marketing Directors
Brand Developers
Export Directors
Brand Managers

Industry/Entity Type

Marketing

Number of Pages Required

2 pages

Requirements
Must have
• This design will be integrated into wordpress, I have attached a wireframe of what we need, this is NOT a strict guide but contains content that is essential, the wireframes shows the priority of statements and products. the images supplied need to sell the products and services.
The main banner will eventually be animated so this needs to be taken into account.
The cliemt has supplied images which will need to be used in the design , however if you feel you have better images in the same style then they can be used.
Nice to have
• animation included, Jquery
Should not have
• NO fully flash sites or designs, this site will be Search engine optimised and updateable

```html
<!DOCTYPE html>
<html lang="en">
<head>
<meta charset="utf-8">
<title>Proof &amp; Palate — home and info page proposals</title>
<link href="https://fonts.googleapis.com/css2?family=Arimo:ital,wght@0,400;0,700;1,400;1,700&family=Nunito:wght@800&family=Shadows+Into+Light&display=swap" rel="stylesheet">
<style>
:root{
  --blue:#0aa7da;
  --blue-deep:#1596c3;
  --ink:#222;
  --body:#666;
  --muted:#888;
  --line:#d6d6d6;
  --band:#f3f3f3;
  --white:#fff;
}
*{margin:0;padding:0;box-sizing:border-box}
html,body{width:1200px;height:2421px;overflow:hidden;background:var(--white)}
body{font-family:"Arimo",Arial,sans-serif;color:var(--body)}
.board{width:1152px;height:2324px;position:relative;transform:scale(1.0417);transform-origin:0 0}
.hatch{position:absolute;left:0;width:1152px;height:6px;background:repeating-linear-gradient(135deg,#d4d4d4 0 1px,#fff 1px 3px)}
.page{position:absolute;left:0;width:1152px}
.abs{position:absolute}

.brand{left:488px;top:40px;width:176px;display:flex;align-items:center;gap:8px;font-weight:700;font-size:14px;color:var(--ink);letter-spacing:.2px}
.brand-dot{width:12px;height:12px;border-radius:50%;background:var(--blue);flex:none}
.follow{left:127px;top:99px;font-size:11px;color:#555;display:flex;align-items:center;gap:6px}
.follow .soc{width:15px;height:15px;background:var(--blue);border-radius:2px}
.follow .soc:first-of-type{margin-left:4px;background:#3b5a99}
.contact{left:851px;top:99px;font-size:11px;line-height:14px;color:#555}
.contact b{color:var(--ink)}
.contact a{color:#555}

.nav-rule{left:0;width:1152px;height:1px;background:var(--line)}
.nav a{position:absolute;top:19px;font-size:15px;color:var(--ink);text-decoration:none;white-space:nowrap}
.nav .active{top:4px;height:48px;padding:0 22px;line-height:48px;background:var(--blue);color:var(--white);font-weight:700}
.nav .active::after{content:"";position:absolute;left:50%;bottom:-8px;margin-left:-7px;border:7px solid transparent;border-bottom:0;border-top-color:var(--blue);border-top-width:8px}

.band{left:0;width:1152px;background:var(--band);border-top:1px solid #e6e6e6;border-bottom:1px solid #e6e6e6}
.visual{background:linear-gradient(180deg,#fafafa,#e4e4e4 60%,#f0f0f0)}
.quote{left:564px;top:304px;font-family:"Nunito",sans-serif;font-weight:800;font-size:39px;line-height:48px;color:var(--blue-deep)}
.sig{right:232px;top:452px;text-align:right;font-family:"Shadows Into Light",cursive;font-size:30px;line-height:32px;color:#8a8a8a}
.chev{width:34px;height:50px}

.feature{width:272px}
.feature svg{position:absolute;left:0;top:4px}
.feature h3{margin-left:36px;font-weight:400;font-size:24px;line-height:30px;color:var(--ink)}
.feature p{margin:14px 0 0 39px;font-size:11px;line-height:17px;color:var(--body)}
.more{display:block;text-align:right;margin-top:17px;font-size:12px;font-weight:700;color:var(--blue);text-decoration:underline}
.more::after{content:"";display:inline-block;margin-left:6px;border:4px solid transparent;border-right:0;border-left:5px solid var(--blue);vertical-align:0}

.foot-rule{left:126px;width:900px;height:1px;background:var(--line)}
.keywords{left:0;width:1152px;text-align:center;font-size:11px;font-weight:700;color:#555;word-spacing:1px}
.keywords span{font-weight:400;margin:0 4px;color:#777}
.copy{left:0;width:1152px;text-align:center;font-size:10px;color:#555}
.label{left:0;width:1152px;text-align:center;font-family:"Arimo",sans-serif;font-weight:700;font-size:30px;color:#666}

.title{left:158px;font-family:"Nunito",sans-serif;font-weight:800;font-size:40px;color:var(--blue-deep)}
.photo{left:126px;width:269px;height:424px;border:3px solid #1b1b1b;background:linear-gradient(160deg,#3a2a22,#7e5a44 40%,#d8d8dc 62%,#3c3ec0 82%,#5a3a2a)}
.caption{left:147px;font-size:10px;line-height:14px;font-style:italic;color:#888;width:220px}
.article{left:425px;width:603px;font-size:11px;line-height:17px;color:var(--body)}
.article .lead{font-weight:700;font-style:italic;color:#555}
.article .sub{font-weight:700;color:#555;margin-top:17px}
.ticks{list-style:none;margin:12px 0 0 20px}
.ticks li{position:relative;padding-left:16px;margin-bottom:13px}
.ticks li svg{position:absolute;left:0;top:3px}
.ticks em{color:var(--blue-deep)}
.article .close{margin-top:30px}
</style>
</head>
<body>
<div class="board">

  <!-- HOME PAGE -->
  <section class="page" style="top:0;height:1065px">
    <div class="hatch" style="top:0"></div>
    <div class="abs brand"><span>PROOF &amp; PALATE</span><span class="brand-dot"></span></div>
    <div class="abs follow">Follow us: <span class="soc" role="img" aria-label="Social profile"></span><span class="soc" role="img" aria-label="Social profile"></span></div>
    <div class="abs contact"><b>T:</b> 020 7946 0183<br><b>E:</b> <a>info@proofandpalate.com</a></div>

    <div class="abs nav-rule" style="top:156px"></div>
    <nav class="abs nav" style="top:156px;left:0;width:1152px;height:56px">
      <a class="active" style="left:126px">home</a>
      <a style="left:239px">proof &amp; palate</a>
      <a style="left:411px">a little about us</a>
      <a style="left:566px">our spirit marketing</a>
      <a style="left:749px">big brand success</a>
      <a style="left:926px">speak to us</a>
    </nav>
    <div class="abs nav-rule" style="top:212px"></div>

    <div class="abs band" style="top:213px;height:400px"></div>
    <div class="abs visual" style="left:262px;top:242px;width:196px;height:338px;border-radius:6px" role="img" aria-label="Martini glass with olives on a cocktail stick"></div>
    <svg class="abs chev" style="left:126px;top:392px" viewBox="0 0 34 50"><path d="M30 2 L6 25 L30 48" fill="none" stroke="#1e1e1e" stroke-width="7"/></svg>
    <svg class="abs chev" style="left:994px;top:392px" viewBox="0 0 34 50"><path d="M4 2 L28 25 L4 48" fill="none" stroke="#1e1e1e" stroke-width="7"/></svg>
    <blockquote class="abs quote">“turning our small<br>time whisky into a<br>national brand”</blockquote>
    <div class="abs sig">Daniel Hartley<br>Norvessa</div>

    <div class="abs feature" style="left:126px;top:642px">
      <svg width="28" height="40" viewBox="0 0 28 40"><path d="M1 2 H27 Q24 14 14 16 Q4 14 1 2Z" fill="#c8c8c8"/><rect x="13" y="16" width="2" height="22" fill="#d4d4d4"/></svg>
      <h3>22 years experience with big brands</h3>
      <p>Lorem ipsum dolor sit amet, consectetur adipiscing elit. Aliquam id nisi nisi. Sed non erat nisi. Nam tincidunt diam ultrices tellus hendrerit vehicula vel sit amet.</p>
      <a class="more">READ MORE</a>
    </div>
    <div class="abs feature" style="left:442px;top:642px">
      <svg width="28" height="40" viewBox="0 0 28 40"><path d="M1 2 H27 Q24 14 14 16 Q4 14 1 2Z" fill="#c8c8c8"/><rect x="13" y="16" width="2" height="22" fill="#d4d4d4"/></svg>
      <h3>Marketing your drink the next big brand</h3>
      <p>Lorem ipsum dolor sit amet, consectetur adipiscing elit. Aliquam id nisi nisi. Sed non erat nisi. Nam tincidunt diam ultrices tellus hendrerit vehicula vel sit amet.</p>
      <a class="more">READ MORE</a>
    </div>
    <div class="abs feature" style="left:756px;top:642px">
      <svg width="28" height="40" viewBox="0 0 28 40"><path d="M1 2 H27 Q24 14 14 16 Q4 14 1 2Z" fill="#c8c8c8"/><rect x="13" y="16" width="2" height="22" fill="#d4d4d4"/></svg>
      <h3>350 outlets that listen to what we say</h3>
      <p>Lorem ipsum dolor sit amet, consectetur adipiscing elit. Aliquam id nisi nisi. Sed non erat nisi. Nam tincidunt diam ultrices tellus hendrerit vehicula vel sit amet.</p>
      <a class="more">READ MORE</a>
    </div>

    <div class="abs foot-rule" style="top:859px"></div>
    <div class="abs keywords" style="top:878px">brand marketing<span>|</span>brand marketing strategy<span>|</span>drinks marketing<span>|</span>spirits marketing<span>|</span>alcohol drinks marketing<span>|</span>drinks brand development</div>
    <div class="abs copy" style="top:905px">© 1999 - 2010 Proof &amp; Palate | Terms &amp; Conditions | Privacy Policy</div>
    <div class="hatch" style="top:947px"></div>
    <div class="abs label" style="top:978px">home page - proposal</div>
  </section>

  <!-- INFO PAGE -->
  <section class="page" style="top:1065px;height:1259px">
    <div class="hatch" style="top:0"></div>
    <div class="abs brand"><span>PROOF &amp; PALATE</span><span class="brand-dot"></span></div>
    <div class="abs follow">Follow us: <span class="soc" role="img" aria-label="Social profile"></span><span class="soc" role="img" aria-label="Social profile"></span></div>
    <div class="abs contact"><b>T:</b> 020 7946 0183<br><b>E:</b> <a>info@proofandpalate.com</a></div>

    <div class="abs nav-rule" style="top:156px"></div>
    <nav class="abs nav" style="top:156px;left:0;width:1152px;height:56px">
      <a style="left:148px">home</a>
      <a style="left:236px">proof &amp; palate</a>
      <a class="active" style="left:387px">a little about us</a>
      <a style="left:574px">our spirit marketing</a>
      <a style="left:757px">big brand success</a>
      <a style="left:934px">speak to us</a>
    </nav>
    <div class="abs nav-rule" style="top:212px"></div>

    <div class="abs band" style="top:213px;height:95px"></div>
    <h1 class="abs title" style="top:234px">a little about us</h1>

    <div class="abs photo" style="top:339px" role="img" aria-label="Cocktail glass with a physalis garnish on a bar counter"></div>
    <div class="abs caption" style="top:771px">A caption goes here lorem impum dolor sit amet consecterut adisipson</div>

    <article class="abs article" style="top:336px">
      <p><span class="lead">Lorem ipsum dolor sit amet, consectetur adipiscing elit. Nulla elementum, ligula in porta adipiscing, arcu velit tincidunt nulla, in luctus nisi risus malesuada elit. Mauris interdum justo massa, at pellentesque metus. Morbi dignissim tempor tellus vitae mattis. Vestibulum augue nisl, semper non vulputate imperdiet, commodo sollicitudin lacus.</span> Nam orci massa, faucibus quis lacinia a, tempus at turpis. Pellentesque faucibus felis sed orci sodales ut faucibus arcu iaculis. Nullam in eros risus. Sed varius metus sit amet nibh faucibus pulvinar. Pellentesque habitant morbi tristique senectus et netus et malesuada fames ac turpis egestas. In leo lorem, dapibus ut rutrum eu, tincidunt ut odio. Nulla at mauris vel nisl interdum adipiscing quis at orci. Aliquam ut metus est. Morbi commodo faucibus lorem, et malesuada ante laoreet id. Vestibulum eu ornare orci. Nunc cursus adipiscing augue. Aliquam ultricies lectus ac arcu hendrerit pharetra. Nullam tincidunt tristique mauris sed varius. Proin massa nisi, feugiat at cursus eu, faucibus ut felis. Maecenas ac pretium orci. Suspendisse rutrum condimentum erat in ultricies.</p>
      <p class="sub">Sed elit magna, accumsan sed varius vel, faucibus sed lectus. Aenean fermentum risus quis ligula feugiat pulvinar.</p>
      <ul class="ticks">
        <li><svg width="11" height="9" viewBox="0 0 11 9"><path d="M1 4.5 L4 7.5 L10 1" fill="none" stroke="#0aa7da" stroke-width="2.2"/></svg><em>Sed sit amet quam id lorem aliquam facilisis.</em> Nam tincidunt faucibus ligula, id consectetur arcu vulputate eu. Mauris at ante libero, vel pellentesque arcu.</li>
        <li><svg width="11" height="9" viewBox="0 0 11 9"><path d="M1 4.5 L4 7.5 L10 1" fill="none" stroke="#0aa7da" stroke-width="2.2"/></svg><em>Donec commodo libero lorem.</em> Aliquam tellus leo, aliquet a porttitor fermentum, bibendum laoreet erat. Proin iaculis luctus ultricies.</li>
        <li><svg width="11" height="9" viewBox="0 0 11 9"><path d="M1 4.5 L4 7.5 L10 1" fill="none" stroke="#0aa7da" stroke-width="2.2"/></svg><em>Mauris in augue tellus, id luctus magna.</em> Nulla tempor vehicula fringilla. Nunc nec felis vitae leo facilisis dapibus. Nam eget urna nec orci varius imperdiet.</li>
      </ul>
      <p class="close">Mauris et velit leo. Nulla sem ligula, accumsan non tincidunt non, blandit eget elit. Ut auctor tellus id mauris malesuada eget interdum dolor tincidunt. Nunc eget augue a turpis venenatis euismod. Integer ultrices cursus diam et pharetra. Quisque sed est ante. Integer nunc mi, accumsan quis pretium vitae, vulputate sed leo. Aenean porttitor nisi sollicitudin diam rutrum vel suscipit mauris commodo.</p>
    </article>

    <div class="abs feature" style="left:126px;top:857px">
      <svg width="28" height="40" viewBox="0 0 28 40"><path d="M1 2 H27 Q24 14 14 16 Q4 14 1 2Z" fill="#c8c8c8"/><rect x="13" y="16" width="2" height="22" fill="#d4d4d4"/></svg>
      <h3>22 years experience with big brands</h3>
      <p>Lorem ipsum dolor sit amet, consectetur adipiscing elit. Aliquam id nisi nisi. Sed non erat nisi. Nam tincidunt diam ultrices tellus hendrerit vehicula vel sit amet.</p>
      <a class="more">READ MORE</a>
    </div>
    <div class="abs feature" style="left:442px;top:857px">
      <svg width="28" height="40" viewBox="0 0 28 40"><path d="M1 2 H27 Q24 14 14 16 Q4 14 1 2Z" fill="#c8c8c8"/><rect x="13" y="16" width="2" height="22" fill="#d4d4d4"/></svg>
      <h3>Marketing your drink the next big brand</h3>
      <p>Lorem ipsum dolor sit amet, consectetur adipiscing elit. Aliquam id nisi nisi. Sed non erat nisi. Nam tincidunt diam ultrices tellus hendrerit vehicula vel sit amet.</p>
      <a class="more">READ MORE</a>
    </div>
    <div class="abs feature" style="left:756px;top:857px">
      <svg width="28" height="40" viewBox="0 0 28 40"><path d="M1 2 H27 Q24 14 14 16 Q4 14 1 2Z" fill="#c8c8c8"/><rect x="13" y="16" width="2" height="22" fill="#d4d4d4"/></svg>
      <h3>350 outlets that listen to what we say</h3>
      <p>Lorem ipsum dolor sit amet, consectetur adipiscing elit. Aliquam id nisi nisi. Sed non erat nisi. Nam tincidunt diam ultrices tellus hendrerit vehicula vel sit amet.</p>
      <a class="more">READ MORE</a>
    </div>

    <div class="abs foot-rule" style="top:1075px"></div>
    <div class="abs keywords" style="top:1094px">brand marketing<span>|</span>brand marketing strategy<span>|</span>drinks marketing<span>|</span>spirits marketing<span>|</span>alcohol drinks marketing<span>|</span>drinks brand development</div>
    <div class="abs copy" style="top:1121px">© 1999 - 2010 Proof &amp; Palate | Terms &amp; Conditions | Privacy Policy</div>
    <div class="hatch" style="top:1163px"></div>
    <div class="abs label" style="top:1194px">info page - proposal</div>
  </section>

</div>
</body>
</html>
```